Wren Hollow Honey Label Design

I need to design a label for my honey

Wren Hollow Honey - 100% Raw Natural Australian Honey from Flowerdale Victoria

I like clean uncluttered designs - ideally with a hexagon background to tie into the hive - not garish or too brightly coloured, classic to the point of being understated.
Would like the label to be a wrap around for our 500G jars

Label size is

face - 4CM
Height 6.5CM
Wrap around dimension 16 CM (corners are rounded)

Would like to include the "produce of Australia Logo on the side - image here https://www.tradesignsregistry.example/files/originlabelsjpg

Possibly some text on one of the sides also along the lines of

Natures gold from the Shire of Murrindindi. Our bees live and work in the beautiful countryside of Flowerdale, Victoria. We are an independent 100% Australian owned honey producer. our honey is made as nature intended, nothing added, taken away or blended with it, just pure raw natural honey. for more information or enquiries please drop us a line at wrenhollowhoney@example-mail.net

Our hives are in the countryside in Flowerdale and there are lots of parrots, Lorikeets and Cockatoos - the king parrots are particularly prevalent and we would very much like them to feature in the logo and be prominent in the label design

if it helps or you are looking for images of bees - I am a photographer and have some images of bees - are than happy to provide these in whatever formate works - here are some of my images https://www.snapgallery.example/member/Dmoorelens

Target Market(s)

People looking to purchase pure Australian honey, unadulterated and guaranteed 100% natural

Logo Text

Wren Hollow Honey, ( natures gold from Flowerdale) optional

Font styles to use
Decorative

Colors

Designer to choose colors to be used in the design.

Requirements
Must have
• A wren Hollow image (male green and red)
• uncluttered and clean image
• connection to nature and natural products
• Australian owned and produced
• Natural product
• Independent, Victorian ethical honey producer
• must look and feel all local business
• Sorry should have stated that the jars are 500gms, they will contain 500 grams of Honey
• Please see guidance for honey labelling
• https://bellcreekapiary.example/honey-labelling/
• regarding the nutritional content, we will need to include this
• I would also like to have a small section "Packed __/__/__ Batch____" to allow me to then insert a date in order to track product
• Wren Hollow Honey
• 4183 Tarnwick-Elby Road. Flowerdale. Victoria. 3717
Nice to have
• Hexagon background design to tie it to the bees
• Calorific content of honey, this can be found on the web easy enough
• I like the idea/concept of a gauge on the side of one of the side panels that shows people how much honey they have left and of course when it gets down to the bottom of the label suggests they get some more before they run out
Should not have
• lots of clashing vibrant colours - need to be classically understated and clean
• Must not be corporate, big business

```html
<!DOCTYPE html>
<html lang="en">
<head>
<meta charset="utf-8">
<title>Wren Hollow Honey – 500g Jar Label</title>
<link rel="stylesheet" href="https://fonts.googleapis.com/css2?family=Marcellus&family=Crimson+Text:ital,wght@0,700;1,400;1,700&family=Arimo:wght@400;700&display=swap">
<style>
  :root {
    --honey-light: #fde36a;
    --honey-mid: #fbcf2c;
    --honey-deep: #f2a90f;
    --ink: #3b3633;
    --ink-soft: #4a4440;
    --text-dark: #2b2620;
    --table-head: #f6b25a;
    --table-body: #fbd48d;
    --badge-green: #2f7d3b;
    --badge-gold: #f3c323;
    --mark: #5b8f2e;
  }
  * { box-sizing: border-box; margin: 0; padding: 0; }
  html, body { width: 1200px; height: 488px; overflow: hidden; }
  body { background: #ffffff; }

  .label {
    position: relative;
    width: 1200px;
    height: 488px;
    overflow: hidden;
    background: radial-gradient(ellipse 60% 80% at 50% 40%, var(--honey-light) 0%, var(--honey-mid) 55%, var(--honey-deep) 100%);
    font-family: "Arimo", Arial, sans-serif;
    color: var(--text-dark);
  }

  .story {
    position: absolute;
    left: 40px;
    top: 50px;
    width: 358px;
    font-size: 12.5px;
    line-height: 19.5px;
    text-align: justify;
  }

  .origin-badge {
    position: absolute;
    left: 40px;
    top: 204px;
    width: 62px;
    height: 102px;
    background: #ffffff;
    border: 2px solid var(--badge-green);
    border-radius: 3px;
  }
  .origin-badge span {
    position: absolute;
    left: 7px; top: 8px; right: 7px; height: 58px;
    background: var(--badge-gold);
    border-radius: 2px;
  }

  .brand-dot {
    position: absolute;
    left: 565px;
    top: 46px;
    width: 70px;
    height: 70px;
    border-radius: 50%;
    background: var(--mark);
  }
  .brand-name {
    font-family: "Marcellus", Georgia, serif;
    font-weight: 400;
    color: var(--ink);
  }
  .brand-name span {
    position: absolute;
    left: 0;
    width: 1200px;
    text-align: center;
    line-height: 1;
  }
  .brand-name .line-top { top: 126px; font-size: 42px; }
  .brand-name .line-main { top: 170px; font-size: 84px; letter-spacing: 1px; }

  .tagline {
    position: absolute;
    left: 0;
    width: 1200px;
    text-align: center;
    font-family: "Crimson Text", Georgia, serif;
    font-style: italic;
    color: var(--ink-soft);
    line-height: 1;
  }
  .tagline.first { top: 253px; font-size: 17px; font-weight: 700; }
  .tagline.second { top: 286px; font-size: 18px; font-weight: 400; letter-spacing: 0.5px; }

  .nutrition {
    position: absolute;
    left: 914px;
    top: 30px;
    width: 252px;
    font-size: 8.5px;
    border-collapse: collapse;
  }
  .nutrition caption {
    text-align: left;
    background: var(--table-head);
    font-weight: 700;
    padding: 3px 5px;
    font-size: 8.5px;
  }
  .nutrition td {
    background: var(--table-body);
    padding: 3px 4px;
    border-top: 1px solid #f7e2b6;
    white-space: nowrap;
  }
  .nutrition td.v { text-align: right; padding-right: 7px; }
  .approx {
    position: absolute;
    left: 1090px;
    top: 118px;
    font-size: 7px;
    color: #5b5246;
  }

  .contact {
    position: absolute;
    left: 893px;
    top: 146px;
    width: 290px;
    text-align: center;
    font-style: normal;
    font-size: 11.5px;
    font-weight: 700;
    line-height: 16.6px;
  }

  .batch {
    position: absolute;
    left: 930px;
    top: 216px;
    font-family: "Crimson Text", Georgia, serif;
    font-weight: 700;
    font-size: 17px;
    line-height: 23px;
    color: var(--text-dark);
  }

  .comb {
    position: absolute;
    left: 0;
    top: 300px;
    width: 1200px;
    height: 188px;
  }

  .net-weight {
    position: absolute;
    left: 0;
    width: 1200px;
    top: 440px;
    text-align: center;
    font-family: "Crimson Text", Georgia, serif;
    font-weight: 700;
    font-size: 19px;
    color: var(--text-dark);
  }
</style>
</head>
<body>
<main class="label">

  <p class="story">Natures gold from the Shire of Murrindindi. Our bees live and work in the beautiful countryside of Flowerdale, Victoria. We are an independent 100% Australian owned honey producer. our honey is made as nature intended, nothing added, taken away or blended with it, just pure raw natural honey. for more information or enquiries please drop us a line at wrenhollowhoney@example-mail.net</p>

  <div class="origin-badge" role="img" aria-label="Country of origin badge"><span></span></div>

  <span class="brand-dot" aria-hidden="true"></span>
  <h1 class="brand-name"><span class="line-top">WREN HOLLOW</span><span class="line-main">HONEY</span></h1>

  <p class="tagline first">100% Raw Natural Australian</p>
  <p class="tagline second">Honey from Flowerdale Victoria</p>

  <table class="nutrition">
    <caption>NUTRITIONAL FACTS* Per 100g</caption>
    <tr><td>Energy</td><td class="v">320kcal</td><td>Protein</td><td class="v">0g</td><td>Calcium</td><td class="v">13mg</td></tr>
    <tr><td>Carbohydrate</td><td class="v">80g</td><td>Fat</td><td class="v">0g</td><td>Iron</td><td class="v">1.5mg</td></tr>
    <tr><td>Natural Sugar</td><td class="v">80g</td><td>Sodium</td><td class="v">17mg</td><td>Phosphorus</td><td class="v">5mg</td></tr>
    <tr><td>Added Sugar</td><td class="v">0g</td><td>Potassium</td><td class="v">138mg</td><td></td><td></td></tr>
  </table>
  <p class="approx">*Approximate Values</p>

  <address class="contact">
    To learn more about our products and passions,<br>
    visit: www.wrenhollowhoney.example<br>
    email:wrenhollow@honeyjar.example,<br>
    Ph: +61355501827
  </address>

  <div class="batch">
    Packed<br>
    Batch No<br>
    Wren Hollow Honey<br>
    #4183 Tarnwick-Elby Road.<br>
    Flowerdale. Victoria. 3717
  </div>

  <svg class="comb" viewBox="0 0 1200 188" role="img" aria-label="Honeycomb with flowing honey drips" preserveAspectRatio="none">
    <defs>
      <linearGradient id="comb-fill" x1="0" y1="0" x2="0" y2="1">
        <stop offset="0" stop-color="#fff3a6"/>
        <stop offset="0.35" stop-color="#fcd33a"/>
        <stop offset="1" stop-color="#f0a20c"/>
      </linearGradient>
    </defs>
    <path d="M0 40 C120 10 240 60 360 45 C460 32 520 24 600 8 C680 24 740 32 840 45 C960 60 1080 10 1200 40 L1200 188 L0 188 Z" fill="url(#comb-fill)"/>
  </svg>

  <p class="net-weight">500gms</p>

</main>
</body>
</html>
```